Commercial Insurance Agency needs a design for a trade show retractable display.

We need a design for a retractable banner or display for a trade show. We are a commercial insurance agency that specializes in placing and servicing workers comp insurance for large companies. We want to use our company colors which are orange, grey and charcoal.

Font styles to use
Sans Serif

Requirements
Must have
• Our orange color that is on the style sheet should be the secondary color...we don't want the whole thing to be orange

```html
<!DOCTYPE html>
<html lang="en">
<head>
<meta charset="utf-8">
<title>Coverpoint – Trade Show Banner</title>
<link href="https://fonts.googleapis.com/css2?family=Roboto+Condensed:wght@300;400;700&display=swap" rel="stylesheet">
<style>
  :root {
    --stage: #9b9b9b;
    --charcoal: #55575a;
    --grey-mid: #7b7c7e;
    --grey-light: #a8a9aa;
    --icon-disc: #c9cacb;
    --orange: #ef5a24;
    --orange-top: #f47a20;
    --orange-deep: #e8431f;
    --white: #ffffff;
    --body-text: #6d6e70;
  }
  * { box-sizing: border-box; margin: 0; padding: 0; }
  html, body { width: 1200px; height: 1200px; overflow: hidden; }
  body {
    background: radial-gradient(ellipse at center, #b3b3b3 0%, var(--stage) 70%);
    font-family: "Roboto Condensed", Arial, sans-serif;
  }
  .banner {
    position: absolute;
    left: 380px; top: 40px;
    width: 440px; height: 1120px;
    background: var(--white);
    overflow: hidden;
    box-shadow: 0 10px 30px rgba(0,0,0,.25);
  }
  .hero {
    position: absolute; left: 0; top: 0;
    width: 440px; height: 575px;
    background:
      radial-gradient(ellipse at 42% 45%, #6e6a5f 0%, transparent 45%),
      linear-gradient(180deg, #9a9690 0%, #7d7a72 35%, #5b5f63 70%, #3d4652 100%);
  }
  .brand-name {
    position: absolute; right: 24px; top: 94px;
    color: var(--white); font-weight: 700; font-size: 30px; letter-spacing: 1px;
  }
  .accent-bar {
    position: absolute; background: var(--orange); height: 40px; top: 480px;
  }
  .accent-bar.left { left: 0; width: 114px; }
  .accent-bar.right { right: 0; width: 16px; }
  .headline {
    position: absolute; right: 30px; top: 440px;
    color: var(--white); font-weight: 700; font-size: 34px; line-height: 34px;
    text-align: right; letter-spacing: -0.3px;
  }
  .services {
    position: absolute; left: 0; top: 575px; width: 440px; height: 180px;
    display: flex;
  }
  .service {
    display: flex; flex-direction: column; align-items: center;
    padding-top: 36px;
  }
  .service.compliance { width: 162px; background: var(--charcoal); }
  .service.claims { width: 138px; background: var(--grey-mid); }
  .service.profit { width: 140px; background: var(--grey-light); }
  .service-icon {
    width: 70px; height: 70px; border-radius: 50%;
    background: var(--icon-disc);
    display: flex; align-items: center; justify-content: center;
  }
  .service-title {
    margin-top: 34px; color: var(--white); font-size: 22px; font-weight: 700;
  }
  .details {
    position: absolute; left: 0; top: 755px; width: 440px;
    display: flex;
  }
  .detail {
    color: var(--body-text); font-size: 14px; font-weight: 300; line-height: 17px;
    text-align: center; padding-top: 30px;
  }
  .detail:nth-child(1) { width: 162px; }
  .detail:nth-child(2) { width: 138px; }
  .detail:nth-child(3) { width: 140px; }
  .footer-band { position: absolute; left: 0; top: 905px; }
  .site-url {
    position: absolute; left: 0; width: 440px; top: 1060px;
    text-align: center; color: var(--white); font-weight: 700; font-size: 17px;
  }
</style>
</head>
<body>
  <main class="banner">
    <section class="hero" role="img" aria-label="Photo of a factory worker in a yellow hard hat and overalls holding a coffee cup in a workshop"></section>

    <div class="brand-name">COVERPOINT</div>

    <div class="accent-bar left"></div>
    <div class="accent-bar right"></div>
    <h1 class="headline">Reduce<br>Employers’ Workers’<br>Compensation Cost</h1>

    <section class="services">
      <div class="service compliance">
        <div class="service-icon">
          <svg width="30" height="34" viewBox="0 0 30 34" fill="#fff">
            <circle cx="15" cy="6" r="5"/>
            <rect x="12" y="10" width="6" height="10"/>
            <rect x="4" y="20" width="22" height="6" rx="2"/>
            <rect x="6" y="29" width="18" height="3" rx="1.5"/>
          </svg>
        </div>
        <div class="service-title">Compliance</div>
      </div>
      <div class="service claims">
        <div class="service-icon">
          <svg width="34" height="30" viewBox="0 0 34 30" fill="none" stroke="#fff" stroke-width="2.5">
            <rect x="3" y="10" width="24" height="14" rx="2"/>
            <path d="M6 6h22M9 2h16"/>
            <circle cx="15" cy="17" r="3.5"/>
            <circle cx="27" cy="22" r="5" fill="#fff"/>
          </svg>
        </div>
        <div class="service-title">Claims</div>
      </div>
      <div class="service profit">
        <div class="service-icon">
          <svg width="28" height="32" viewBox="0 0 28 32" fill="none" stroke="#fff" stroke-width="2.5">
            <path d="M6 2h12l7 7v21H6z"/>
            <path d="M12 14h9M12 20h9M12 26h9"/>
            <circle cx="4" cy="17" r="3"/>
          </svg>
        </div>
        <div class="service-title">Profit Leaks</div>
      </div>
    </section>

    <section class="details">
      <p class="detail">Training and<br>Certifications<br>HR and Safety<br>Onsite Compliance<br>Audits</p>
      <p class="detail">Immediate,<br>Ongoing Injury<br>and Claims<br>Management</p>
      <p class="detail">Detect and Correct<br>Profit Leaks Inherent<br>in Every Work Comp<br>Program That Drives<br>the Cost</p>
    </section>

    <svg class="footer-band" width="440" height="215" viewBox="0 0 440 215">
      <defs>
        <linearGradient id="footerFill" x1="0" y1="0" x2="0" y2="1">
          <stop offset="0" stop-color="#f47a20"/>
          <stop offset="1" stop-color="#e8431f"/>
        </linearGradient>
      </defs>
      <path d="M0 20 Q220 60 440 0 L440 215 L0 215 Z" fill="url(#footerFill)"/>
    </svg>
    <div class="site-url">www.coverpointagency.com</div>
  </main>
</body>
</html>
```